Bravel Acres Business Cards

design business cards for our new business should match my Corvane Quotations business cards

Contact Information for Business Card

2817 W 68th N St
Pellston, KS 74592

Requirements
Must have
• should match logo colors

```html
<!DOCTYPE html>
<html lang="en">
<head>
<meta charset="utf-8">
<title>Bravel Acres Business Cards</title>
<link rel="stylesheet" href="https://fonts.googleapis.com/css2?family=Poppins:wght@400;500;600;700&display=swap">
<style>
  :root {
    --stage: #e7eaeb;
    --card-dark: #0f2b31;
    --card-dark-soft: #17373d;
    --brand-green: #62bb46;
    --brand-teal: #1aa9a6;
    --ink-light: #ffffff;
    --divider: #5f7a7f;
    --paper: #ffffff;
    --pattern-tint: #e9f4f3;
    --edge-dark: #0f2b31;
  }
  * { box-sizing: border-box; margin: 0; padding: 0; }
  html, body {
    width: 1200px; height: 900px; overflow: hidden;
    background: var(--stage);
    font-family: "Poppins", sans-serif;
  }
  .sheet {
    width: 1200px; height: 900px;
    display: flex; flex-direction: column;
    align-items: center; justify-content: center; gap: 44px;
  }
  .card {
    width: 700px; height: 400px; position: relative; overflow: hidden;
    border-radius: 6px;
    box-shadow: 0 12px 30px rgba(15, 43, 49, 0.22);
  }

  /* Front */
  .card--front { background: var(--card-dark); }
  .front__decor {
    position: absolute; right: -60px; bottom: -80px;
    width: 420px; height: 380px; border-radius: 50%;
    background: radial-gradient(circle, var(--card-dark-soft) 0%, var(--card-dark) 70%);
  }
  .front__brand {
    position: absolute; left: 56px; top: 0; bottom: 0; width: 270px;
    display: flex; align-items: center; justify-content: center;
  }
  .brand-name {
    font-weight: 700; color: var(--brand-green);
    font-size: 42px; line-height: 1.05; letter-spacing: 0.5px; text-align: center;
  }
  .front__divider {
    position: absolute; left: 350px; top: 100px; width: 1px; height: 200px;
    background: var(--divider);
  }
  .front__details {
    position: absolute; left: 384px; top: 0; bottom: 0; width: 290px;
    display: flex; flex-direction: column; justify-content: center;
  }
  .person-name { color: var(--ink-light); font-weight: 600; font-size: 27px; line-height: 1.2; }
  .person-role { color: var(--brand-green); font-weight: 500; font-size: 17px; margin-bottom: 18px; }
  .contact-list { list-style: none; display: flex; flex-direction: column; gap: 8px; }
  .contact-item {
    display: flex; align-items: flex-start; gap: 10px;
    color: var(--ink-light); font-size: 16px; line-height: 1.35;
  }
  .contact-item svg { flex: none; width: 16px; height: 16px; margin-top: 3px; }

  /* Back */
  .card--back { background: var(--paper); }
  .back__pattern { position: absolute; inset: 0; background: var(--pattern-tint); }
  .back__edge { position: absolute; top: 0; bottom: 0; width: 20px; background: var(--edge-dark); }
  .back__edge--left { left: 0; }
  .back__edge--right { right: 0; }
  .back__brand {
    position: absolute; inset: 0;
    display: flex; align-items: center; justify-content: center;
  }
  .back__brand .brand-name { font-size: 52px; color: var(--brand-teal); }
</style>
</head>
<body>
<main class="sheet">
  <section class="card card--front" aria-label="Business card front">
    <div class="front__decor" role="img" aria-label="Large faint leaf decoration"></div>
    <div class="front__brand">
      <p class="brand-name">Bravel Acres</p>
    </div>
    <div class="front__divider"></div>
    <div class="front__details">
      <h1 class="person-name">Dara Whitlow</h1>
      <p class="person-role">Managing Director</p>
      <ul class="contact-list">
        <li class="contact-item">
          <svg viewBox="0 0 24 24" aria-hidden="true"><path fill="var(--brand-green)" d="M6.6 10.8a15.1 15.1 0 0 0 6.6 6.6l2.2-2.2a1 1 0 0 1 1-.25 11.4 11.4 0 0 0 3.6.57 1 1 0 0 1 1 1V20a1 1 0 0 1-1 1A17 17 0 0 1 3 4a1 1 0 0 1 1-1h3.5a1 1 0 0 1 1 1c0 1.25.2 2.45.57 3.6a1 1 0 0 1-.25 1z"/></svg>
          <span>918-555-0142</span>
        </li>
        <li class="contact-item">
          <svg viewBox="0 0 24 24" aria-hidden="true"><rect x="2" y="5" width="20" height="14" rx="2" fill="var(--brand-green)"/><path d="M3 6l9 7 9-7" fill="none" stroke="var(--card-dark)" stroke-width="1.8"/></svg>
          <span>info@bravelacres.com</span>
        </li>
        <li class="contact-item">
          <svg viewBox="0 0 24 24" aria-hidden="true"><path fill="var(--brand-green)" d="M12 2a7 7 0 0 0-7 7c0 5.2 7 13 7 13s7-7.8 7-13a7 7 0 0 0-7-7zm0 9.5A2.5 2.5 0 1 1 12 6.5a2.5 2.5 0 0 1 0 5z"/></svg>
          <span>2817 W 68th N St<br>Pellston, KS 74592</span>
        </li>
      </ul>
    </div>
  </section>

  <section class="card card--back" aria-label="Business card back">
    <div class="back__pattern" role="img" aria-label="Faint repeating brand pattern"></div>
    <div class="back__edge back__edge--left"></div>
    <div class="back__edge back__edge--right"></div>
    <div class="back__brand">
      <p class="brand-name">Bravel Acres</p>
    </div>
  </section>
</main>
</body>
</html>
```